A wine Label for a new brand of New Zealand Wine

We are looking for a Wine Label for our "Harbor Crest" brand of wines from North Otago New Zealand. We would like the label to perhaps use the HC as a logo and the rest up to the designer. We have our vineyards located in the Waitaki Valley New Zealand which is a southern region with mountains and a river flowing past our vineyard. Photos attached of Dramatic Landscape. Also attached is a basic outline of requirements for the front bottle of the label. The rear bottle label will contain writing about the wines background plus statutory regulations on Alc. Vol, bar code etc. Front Label size to be no Larger than 80mm deep by 100 mm wide. The label can be simple or graphic, whatever the designer chooses.
Target Market(s)
New Wine Brand
Look and feel
Each slider illustrates characteristics of the customer's brand and the style your logo design should communicate.

```html
<!DOCTYPE html>
<html lang="en">
<head>
<meta charset="utf-8">
<title>Harbor Crest Pinot Gris Label</title>
<link rel="stylesheet" href="https://fonts.googleapis.com/css2?family=Archivo+Black&family=Libre+Baskerville:wght@700&family=Open+Sans:wght@400&display=swap">
<style>
  :root {
    --backdrop: #e6e4dc;
    --label-black: #0d0d0d;
    --label-white: #ffffff;
    --gold: #b8862a;
    --gold-line: #c9a04a;
    --ink: #111111;
    --sky: #9fd0ea;
    --hill: #8cbf4a;
    --river: #5aa9d6;
  }
  * { margin: 0; padding: 0; box-sizing: border-box; }
  html, body {
    width: 818px;
    height: 1200px;
    overflow: hidden;
    background: var(--backdrop);
  }
  .label {
    position: absolute;
    left: 86px;
    top: 57px;
    width: 645px;
    height: 1085px;
    background: var(--label-black);
  }
  .label-panel {
    position: absolute;
    left: 18px;
    right: 18px;
    top: 118px;
    bottom: 36px;
    background: var(--label-white);
    outline: 3px solid var(--gold-line);
    outline-offset: 3px;
  }
  .top-rule {
    position: absolute;
    left: 18px;
    right: 18px;
    top: 70px;
    height: 3px;
    background: var(--gold-line);
  }
  .brand-mark {
    position: absolute;
    left: 247px;
    top: 33px;
    width: 150px;
    height: 150px;
    background: var(--label-black);
    border: 4px solid var(--gold-line);
    display: flex;
    align-items: center;
    justify-content: center;
    font-family: "Archivo Black", sans-serif;
    font-size: 72px;
    color: var(--gold);
    letter-spacing: -2px;
  }
  .brand-name {
    position: absolute;
    left: 0;
    right: 0;
    top: 205px;
    text-align: center;
    font-family: "Archivo Black", sans-serif;
    font-size: 84px;
    line-height: 88px;
    color: var(--gold);
  }
  .landscape {
    position: absolute;
    left: 70px;
    top: 405px;
    width: 505px;
    height: 375px;
    border-radius: 40px;
    background: linear-gradient(180deg, var(--sky) 0%, #d7ecf4 35%, var(--hill) 55%, #5f9a37 78%, var(--river) 100%);
  }
  .varietal {
    position: absolute;
    left: 0;
    right: 0;
    top: 790px;
    text-align: center;
    font-family: "Libre Baskerville", serif;
    font-weight: 700;
    font-size: 52px;
    color: var(--ink);
  }
  .vintage {
    position: absolute;
    left: 0;
    right: 0;
    top: 858px;
    text-align: center;
    font-family: "Open Sans", sans-serif;
    font-size: 52px;
    color: var(--ink);
  }
  .region {
    position: absolute;
    left: 0;
    right: 0;
    top: 930px;
    text-align: center;
    font-family: "Open Sans", sans-serif;
    font-size: 30px;
    color: var(--ink);
  }
  .origin {
    position: absolute;
    left: 0;
    right: 0;
    top: 996px;
    text-align: center;
    font-family: "Open Sans", sans-serif;
    font-size: 26px;
    color: var(--ink);
  }
</style>
</head>
<body>
  <div class="label">
    <div class="top-rule"></div>
    <div class="label-panel"></div>
    <div class="brand-mark">HC</div>
    <div class="brand-name">Harbor<br>Crest</div>
    <div class="landscape" role="img" aria-label="Painted vineyard landscape with rolling green hills, a tree and a river winding under a blue sky"></div>
    <div class="varietal">PINOT GRIS</div>
    <div class="vintage">2015</div>
    <div class="region">Waitaki Valley — North Otago</div>
    <div class="origin">New Zealand Wine</div>
  </div>
</body>
</html>
```